Custom Monogramming and Retail gifts

We need a Business Card for a monogramming business that offers many retail gift options. We are a home based business that uses social media (Chatterbook,clipboardly and our website) to sell our products. Our target market is college age, high school, baby gifts.
We want a preppy fun look. Monogramming is very popular in the South

Industry/Entity Type

College

Contact Information for Business Card

Threaded N' Charmed
Custom Monogramming and Gifts
5183 Larkmoor Lane
Brindlecove, XA 00412
Mona Prell, Owner
555-214-7390
threadedncharmed.example
threadedncharmed@mailbox.example

```html
<!DOCTYPE html>
<html lang="en">
<head>
<meta charset="utf-8">
<title>Threaded N' Charmed — Business Card</title>
<link rel="stylesheet" href="https://fonts.googleapis.com/css2?family=Arimo:wght@400;700&display=swap">
<style>
  :root {
    --backdrop: #e4e1dc;
    --card: #ffffff;
    --ink: #111111;
    --text-grey: #555555;
    --pink: #e6398a;
    --band-dark: #1a1a1a;
    --band-light: #4a4a4a;
  }
  * { box-sizing: border-box; margin: 0; padding: 0; }
  html, body {
    width: 1200px; height: 1000px; overflow: hidden;
    background: var(--backdrop);
    font-family: "Arimo", Arial, sans-serif;
  }
  .stage {
    width: 1200px; height: 1000px;
    display: flex; align-items: center; justify-content: center;
  }
  .business-card {
    position: relative;
    width: 1050px; height: 600px;
    background: var(--card);
    box-shadow: 0 10px 30px rgba(0,0,0,0.18);
    display: flex;
    overflow: hidden;
  }
  .pattern-band {
    width: 270px; height: 100%; flex: none;
    background: linear-gradient(90deg, var(--band-dark), var(--band-light));
  }
  .card-body {
    flex: 1;
    padding: 78px 40px 0 150px;
  }
  .brand { margin-bottom: 56px; }
  .brand-name {
    display: flex; align-items: center; gap: 16px;
    font-size: 54px; font-weight: 700; color: var(--pink);
    line-height: 1.08;
  }
  .brand-mark {
    width: 22px; height: 22px; border-radius: 50%;
    background: var(--ink); flex: none;
  }
  .brand-tagline {
    margin-top: 16px; margin-left: 38px;
    font-size: 26px; font-weight: 400; color: var(--ink);
    letter-spacing: 1px;
  }
  .contact-list { list-style: none; }
  .contact-item {
    display: flex; align-items: flex-start; gap: 18px;
    font-size: 27px; color: var(--text-grey);
    line-height: 1.25; margin-bottom: 12px;
    white-space: nowrap;
  }
  .contact-item svg { width: 24px; height: 24px; flex: none; margin-top: 4px; fill: var(--ink); }
  .contact-item--address { color: var(--pink); margin-top: 22px; }
</style>
</head>
<body>
<main class="stage">
  <article class="business-card">
    <div class="pattern-band" role="img" aria-label="Black and white chevron zigzag pattern band"></div>
    <section class="card-body">
      <header class="brand">
        <div class="brand-name"><span class="brand-mark"></span><span>Threaded N'<br>Charmed</span></div>
        <div class="brand-tagline">Custom Monogramming</div>
      </header>
      <ul class="contact-list">
        <li class="contact-item">
          <svg viewBox="0 0 24 24" aria-hidden="true"><path d="M6.6 10.8a15 15 0 0 0 6.6 6.6l2.2-2.2c.3-.3.7-.4 1-.2 1.1.4 2.3.6 3.6.6.6 0 1 .4 1 1V20c0 .6-.4 1-1 1A17 17 0 0 1 3 4c0-.6.4-1 1-1h3.5c.6 0 1 .4 1 1 0 1.3.2 2.5.6 3.6.1.3 0 .7-.2 1z"/></svg>
          <span>555-214-7390</span>
        </li>
        <li class="contact-item">
          <svg viewBox="0 0 24 24" aria-hidden="true"><path d="M2 5h20v14H2z M3.5 6.5 12 13l8.5-6.5" fill="none" stroke="#111" stroke-width="2"/></svg>
          <span>threadedncharmed.example</span>
        </li>
        <li class="contact-item">
          <svg viewBox="0 0 24 24" aria-hidden="true"><circle cx="5" cy="19" r="2.5"/><path d="M3 11a10 10 0 0 1 10 10M3 4a17 17 0 0 1 17 17" fill="none" stroke="#111" stroke-width="2.6"/></svg>
          <span>threadedncharmed@mailbox.example</span>
        </li>
        <li class="contact-item contact-item--address">
          <svg viewBox="0 0 24 24" aria-hidden="true"><path d="M12 3 2 12h3v9h5v-6h4v6h5v-9h3z"/></svg>
          <span>5183 Larkmoor Lane Brindlecove<br>XA 00412 Mona Prell</span>
        </li>
      </ul>
    </section>
  </article>
</main>
</body>
</html>
```